electrical company- Company name- Voltmark Trades, slogan- All installations and servicingcolours to stick roughly with logo- greys, blues, black, white. simple yet effective- logo to stand out and attention to name also (gareth). Modern design.

Industry/Entity Type

Business

Contact Information for Business Card

gareth WilliamsElectrician021 994 306info@voltmarktrades.co.nzwww.voltmarktrades.co.nzPO box 5367Palmerston North, 4472

```html
<!DOCTYPE html>
<html lang="en">
<head>
<meta charset="utf-8">
<title>Voltmark Trades — Business Card</title>
<link rel="stylesheet" href="https://fonts.googleapis.com/css2?family=Montserrat:wght@400;500;600;700&display=swap">
<style>
  :root {
    --stage: #e9eaec;
    --card: #ffffff;
    --card-edge: #f1f2f3;
    --blue: #1fa8d6;
    --blue-deep: #1596c4;
    --grey-text: #7d7f82;
    --grey-name: #8b8d90;
    --ink: #1b1c1e;
    --white: #ffffff;
  }
  * { box-sizing: border-box; margin: 0; padding: 0; }
  html, body {
    width: 1200px;
    height: 780px;
    overflow: hidden;
    background: var(--stage);
    font-family: "Montserrat", Arial, sans-serif;
  }
  .canvas {
    width: 1200px;
    height: 780px;
    display: flex;
    align-items: center;
    justify-content: center;
    gap: 70px;
  }
  .card {
    width: 400px;
    height: 650px;
    background: linear-gradient(160deg, var(--card) 0%, var(--card-edge) 100%);
    box-shadow: 0 10px 30px rgba(0,0,0,0.12);
    position: relative;
    display: flex;
    flex-direction: column;
  }

  /* Front */
  .card-front .brand {
    margin-top: 92px;
    display: flex;
    align-items: center;
    justify-content: center;
    gap: 12px;
  }
  .brand-mark {
    width: 22px;
    height: 22px;
    background: var(--blue);
  }
  .brand-name {
    font-weight: 700;
    font-size: 27px;
    letter-spacing: 1px;
    text-transform: uppercase;
    color: var(--blue);
  }
  .person {
    margin-top: 76px;
    text-align: center;
  }
  .person-name {
    font-weight: 600;
    font-size: 31px;
    color: var(--grey-name);
    letter-spacing: 0.5px;
  }
  .person-role {
    margin-top: 2px;
    font-weight: 400;
    font-size: 24px;
    color: var(--blue);
    letter-spacing: 0.5px;
  }
  .contact {
    margin-top: 52px;
    list-style: none;
    text-align: center;
    color: var(--grey-text);
    font-size: 17px;
    line-height: 1.55;
    letter-spacing: 0.4px;
  }
  .contact .phone { font-size: 22px; }
  .contact .address { font-size: 21px; }
  .web-band {
    margin-top: auto;
    height: 88px;
    background: linear-gradient(180deg, var(--blue) 0%, var(--blue-deep) 100%);
    display: flex;
    align-items: center;
    justify-content: center;
  }
  .web-band span {
    color: var(--white);
    font-size: 17px;
    letter-spacing: 0.8px;
  }

  /* Back */
  .card-back {
    align-items: center;
    justify-content: center;
  }
  .card-back .brand {
    display: flex;
    flex-direction: column;
    align-items: center;
    gap: 22px;
  }
  .card-back .brand-mark {
    width: 46px;
    height: 46px;
  }
  .card-back .brand-name {
    font-size: 32px;
    color: var(--ink);
    text-align: center;
    line-height: 1.25;
  }
</style>
</head>
<body>
  <main class="canvas">
    <section class="card card-front" aria-label="Business card front">
      <div class="brand">
        <span class="brand-mark"></span>
        <span class="brand-name">Voltmark Trades</span>
      </div>
      <div class="person">
        <h1 class="person-name">Gareth Pemberly</h1>
        <p class="person-role">Electrician</p>
      </div>
      <ul class="contact">
        <li class="phone">021 573 814</li>
        <li class="email">info@voltmarktrades-example.co.nz</li>
        <li class="address">PO Box 8142</li>
        <li class="address">Palmerston North 4472</li>
      </ul>
      <div class="web-band"><span>www.voltmarktrades-example.co.nz</span></div>
    </section>

    <section class="card card-back" aria-label="Business card back">
      <div class="brand">
        <span class="brand-mark"></span>
        <span class="brand-name">Voltmark<br>Trades</span>
      </div>
    </section>
  </main>
</body>
</html>
```